Brindle Grass Services website design

We want to create a Sports turf website for our business Brindle Grass Services - we do sports turf management on sports fields around the Harlow Bay region soccer rugby league softball fields etc from full turf management plans and maintenance to just supply and apply of turf management products and just supply of products with program we also do grounds facility maintenance at council facility's and grounds that require a higher level of care - we will up load our logos and fonts etc to assist with the colour pallet for the website - we will have to have a landing page a shop page with tabs a gallery tab along with a grants initiative and our coastals finest green tab also - our font for the txt is called ethnocentric
Updates

how do we open time for people to submit we have no one submitted

Industry/Entity Type

Turf

Coding

Coded - Design and coding required

Number of Pages Required

5+ page

Font styles to use
Other font styles liked:
• ethnocentric

Requirements
Must have
• I have mentioned some waffle in the description that should assist
Should not have
• anything not related

```html
<!DOCTYPE html>
<html lang="en">
<head>
<meta charset="utf-8">
<title>Brindle Grass Services | Sports Turf Specialists</title>
<link rel="stylesheet" href="https://fonts.googleapis.com/css2?family=Orbitron:wght@700;900&family=Poppins:wght@400;500;600;700&display=swap">
<style>
:root{
  --green:#2e9b3a;
  --green-dark:#1c5a20;
  --green-deep:#11702f;
  --blue:#1e8fe0;
  --mint:#eef9e1;
  --ink:#1b1f1c;
  --muted:#6b716c;
  --line:#d9e5d6;
  --white:#ffffff;
}
*{box-sizing:border-box;margin:0;padding:0}
html,body{width:1200px;height:5343px;overflow:hidden}
body{font-family:"Poppins",sans-serif;color:var(--ink);background:var(--white);font-size:13px}
.wrap{width:976px;margin:0 auto;position:relative}
.display{font-family:"Orbitron",sans-serif;font-weight:900;letter-spacing:2px;text-transform:uppercase}
.accent{color:var(--blue)}
.btn{display:inline-block;border:2px solid var(--green);color:var(--green);background:var(--white);font-size:11px;font-weight:500;padding:7px 14px;border-radius:4px;white-space:nowrap}
.btn-solid{background:var(--green);color:var(--white)}
.ph{display:block;border-radius:4px}
.section-title{font-size:26px;text-align:center}

/* header */
.site-header{height:64px;display:flex;align-items:center}
.site-header .wrap{display:flex;align-items:center;justify-content:space-between}
.brand{display:flex;align-items:center;gap:7px;font-family:"Orbitron",sans-serif;font-weight:900;font-size:12px;color:var(--green);letter-spacing:.5px;text-transform:uppercase;white-space:nowrap}
.brand i{width:11px;height:11px;background:var(--green);display:block;flex:none}
.nav{display:flex;gap:30px;font-size:11px;align-items:center;white-space:nowrap}
.nav a{color:var(--ink);text-decoration:none}
.nav a.active{color:var(--green)}
.nav .btn{padding:5px 10px}

/* hero */
.hero{height:543px;position:relative;background:linear-gradient(180deg,#1d2a22 0%,#2c4b2f 55%,#4f8a38 100%)}
.hero-text{position:absolute;left:112px;top:136px;color:var(--white);width:560px}
.hero-text .kicker{font-size:12px;margin-bottom:14px}
.hero-text .kicker b{font-family:"Orbitron",sans-serif;color:var(--blue)}
.hero-text h1{font-size:36px;line-height:44px}
.hero-text p{font-size:12px;line-height:18px;margin:16px 0 26px;width:540px}
.hero-text .btn{margin-right:10px}

/* services */
.services{height:450px;padding-top:58px}
.card-row{display:flex;justify-content:space-between;margin-top:34px}
.svc{width:313px;text-align:center}
.svc .ph{height:218px}
.svc h3{font-size:15px;font-weight:600;margin-top:18px}
.arrow{position:absolute;width:24px;height:24px;border:2px solid var(--green);border-radius:4px;display:flex;align-items:center;justify-content:center;color:var(--green);font-size:13px;background:#fff}
.center{text-align:center;margin-top:30px}

/* about */
.about{height:394px;background:var(--mint);padding-top:48px}
.about .wrap{display:flex;gap:72px}
.about .ph{width:444px;height:296px;flex:none}
.about-body{width:400px;padding-top:6px}
.about-body h2{font-size:26px;margin-bottom:16px}
.about-body p{font-size:11px;line-height:16px;color:var(--muted)}
.ticks{list-style:none;margin:12px 0 16px}
.ticks li{font-size:11px;font-weight:500;display:flex;align-items:center;gap:8px;margin-bottom:7px}
.ticks svg{flex:none}

/* how */
.how{height:282px;background:linear-gradient(180deg,#1c4d22,#2d6a2a);color:var(--white);padding-top:38px;position:relative}
.steps{display:flex;justify-content:space-between;margin-top:28px;position:relative}
.step{width:230px;text-align:center;position:relative}
.step h3{font-size:16px;font-weight:600;margin:10px 0 4px}
.step p{font-size:10px;line-height:14px;color:#c9d8c6}
.how-path{position:absolute;left:0;top:0}

/* products */
.products{height:558px;padding-top:58px}
.prod{width:313px;border-radius:6px;box-shadow:0 4px 16px rgba(0,0,0,.09);overflow:hidden;background:#fff}
.prod .ph{height:186px;border-radius:0}
.prod-body{padding:16px 18px 18px}
.prod-body h3{font-size:15px;font-weight:600}
.prod-body p{font-size:10px;line-height:15px;color:var(--muted);margin:8px 0 12px}
.prod-foot{display:flex;justify-content:space-between;align-items:center}
.prod-foot .btn{padding:4px 12px;font-size:10px}
.price{color:var(--green);font-weight:700;font-size:16px}

/* why */
.why{height:414px;background:var(--mint);padding-top:66px}
.why .wrap{display:flex;justify-content:space-between}
.why-body{width:440px;padding-top:22px}
.why-body h2{font-size:26px;margin-bottom:16px}
.why-body>p{font-size:11px;line-height:16px;color:var(--muted)}
.features{display:grid;grid-template-columns:1fr 1fr;gap:20px 24px;margin-top:20px}
.feat{display:flex;gap:10px}
.feat svg{flex:none}
.feat h4{font-size:11px;font-weight:600}
.feat p{font-size:10px;line-height:14px;color:var(--muted)}
.why .ph{width:445px;height:298px}

/* gallery */
.gallery{height:861px;padding-top:60px}
.tabs{display:flex;justify-content:center;gap:10px;margin:28px 0 24px}
.tabs span{border:2px solid var(--green);color:var(--green);font-size:10px;padding:3px 14px;border-radius:3px}
.tabs span.on{background:var(--green);color:#fff}
.grid{display:grid;grid-template-columns:repeat(3,313px);justify-content:space-between;gap:20px 0}
.col{display:flex;flex-direction:column;gap:20px}
.tall{height:373px}
.short{height:186px}

/* blog */
.blog{height:476px}
.post{width:313px}
.post .ph{height:186px}
.date{display:flex;align-items:center;gap:6px;font-size:10px;color:var(--muted);margin:16px 0 6px}
.post h3{font-size:14px;font-weight:600}
.post p{font-size:10px;line-height:15px;color:var(--muted);margin:4px 0}
.more{font-size:10px;color:var(--green);font-weight:600}

/* faq */
.faq{height:519px;background:var(--mint);padding-top:62px}
.faq .wrap{display:flex;justify-content:space-between}
.faq .ph{width:392px;height:394px}
.faq-body{width:540px;padding-top:38px}
.faq-body h2{font-size:26px;margin-bottom:18px}
.q{border-bottom:1px solid var(--line);padding:10px 0 12px}
.q-head{display:flex;justify-content:space-between;font-size:14px;font-weight:600}
.q-head span{color:var(--green);font-weight:400}
.q p{font-size:10px;line-height:14px;color:var(--muted);margin-top:6px}

/* contact */
.contact{height:476px;background:linear-gradient(180deg,#1d4a23,#2d6a2d);padding-top:70px}
.contact .wrap{display:flex;justify-content:space-between}
.form{width:413px;padding-top:60px}
.form h2{color:#fff;font-size:26px;margin-bottom:20px}
.field{border:1px solid rgba(255,255,255,.7);border-radius:3px;color:#e2ece0;font-size:10px;padding:10px 12px;margin-bottom:14px}
.pair{display:flex;gap:12px}
.pair .field{flex:1}
.msg{height:64px}
.map{width:479px;height:328px;border-radius:4px}

/* footer */
.site-footer{height:306px;background:var(--green-deep);color:#fff;padding-top:42px}
.foot-cols{display:flex;justify-content:space-between}
.foot-cols h4{font-family:"Orbitron",sans-serif;font-size:13px;letter-spacing:1.5px;margin-bottom:14px;text-transform:uppercase}
.foot-cols p,.foot-cols li{font-size:10px;line-height:15px;color:#d7ead9}
.foot-cols ul{list-style:none}
.foot-cols li{line-height:21px}
.socials{display:flex;gap:10px;margin-top:18px}
.socials i{width:24px;height:24px;border-radius:50%;background:#fff;display:block}
.news{display:flex;border:1px solid #fff;border-radius:3px;padding:3px;margin-top:16px;width:216px}
.news span{flex:1;font-size:10px;padding:4px 8px;color:#d7ead9}
.news b{background:#fff;color:var(--green);font-size:10px;font-weight:500;padding:4px 14px;border-radius:2px}
.copy{text-align:center;font-size:10px;color:#d7ead9;border-top:1px solid rgba(255,255,255,.25);margin-top:34px;padding-top:14px}
</style>
</head>
<body>

<header class="site-header">
  <div class="wrap">
    <div class="brand"><i></i>Brindle Grass Services</div>
    <nav class="nav">
      <a class="active" href="#">Home</a><a href="#">Our Services</a><a href="#">Gallery</a><a href="#">About Us</a><a href="#">Products</a><a href="#">Blog</a><a href="#">Contact</a>
      <svg width="18" height="16" viewBox="0 0 18 16" fill="none" stroke="#2e9b3a" stroke-width="1.6"><path d="M1 1h3l2 9h9l2-7H5"/><circle cx="7" cy="14" r="1.2"/><circle cx="14" cy="14" r="1.2"/></svg>
      <span class="btn">Request A Quote</span>
    </nav>
  </div>
</header>

<section class="hero">
  <div class="ph" role="img" aria-label="Soccer player's legs striking a ball on a green sports field" style="position:absolute;inset:0;border-radius:0;background:linear-gradient(90deg,rgba(10,20,14,.55),rgba(10,20,14,0))"></div>
  <div class="hero-text">
    <p class="kicker">Welcome to <b>BRINDLE GRASS</b></p>
    <h1 class="display">Performance<br>Starts From<br>The <span class="accent">Ground Up</span></h1>
    <p>At Brindle Grass Services, we combine local knowledge, modern equipment, and premium products to deliver fields that perform at their best season after season.</p>
    <span class="btn">Learn More About Us</span><span class="btn btn-solid">Explore Our Services</span>
  </div>
</section>

<section class="services">
  <div class="wrap">
    <h2 class="display section-title">Our <span class="accent">Services</span></h2>
    <div class="arrow" style="left:-42px;top:150px">&#8249;</div>
    <div class="arrow" style="right:-42px;top:150px">&#8250;</div>
    <div class="card-row">
      <div class="svc"><div class="ph" role="img" aria-label="Coach writing a turf plan on a clipboard" style="background:linear-gradient(160deg,#e9eef0,#7fb257)"></div><h3>Turf Management Planning</h3></div>
      <div class="svc"><div class="ph" role="img" aria-label="Wrapped turf product bales on a field" style="background:linear-gradient(180deg,#3a7fd0 0%,#dfe9ef 45%,#4f9a36 75%)"></div><h3>Supply &amp; Apply Products</h3></div>
      <div class="svc"><div class="ph" role="img" aria-label="Grounds crew maintaining a sports field" style="background:linear-gradient(180deg,#9cc6e6 0%,#5e8a44 40%,#3f7d2f 100%)"></div><h3>Grounds Maintenance</h3></div>
    </div>
    <div class="center"><span class="btn">See All Our Services</span></div>
  </div>
</section>

<section class="about">
  <div class="wrap">
    <div class="ph" role="img" aria-label="Coach on a tree-lined sports field with a ball" style="background:linear-gradient(180deg,#3e7d2f 0%,#6ea24a 55%,#2e7a3a 100%)"></div>
    <div class="about-body">
      <h2 class="display">About <span class="accent">Us</span></h2>
      <p>Founded with a passion for healthy, high-performance sports fields, Brindle Grass Services provides expert turf solutions across Harlow Bay. From full turf management plans and maintenance to product supply and application, we support soccer, rugby league, softball, and council facilities with precision and care.</p>
      <ul class="ticks">
        <li><svg width="12" height="12" viewBox="0 0 12 12"><circle cx="6" cy="6" r="6" fill="#2e9b3a"/><path d="M3.3 6.2l1.8 1.8 3.6-3.8" stroke="#fff" stroke-width="1.4" fill="none"/></svg>Local Harlow Bay turf experts</li>
        <li><svg width="12" height="12" viewBox="0 0 12 12"><circle cx="6" cy="6" r="6" fill="#2e9b3a"/><path d="M3.3 6.2l1.8 1.8 3.6-3.8" stroke="#fff" stroke-width="1.4" fill="none"/></svg>Complete field maintenance</li>
        <li><svg width="12" height="12" viewBox="0 0 12 12"><circle cx="6" cy="6" r="6" fill="#2e9b3a"/><path d="M3.3 6.2l1.8 1.8 3.6-3.8" stroke="#fff" stroke-width="1.4" fill="none"/></svg>Quality turf products &amp; application</li>
        <li><svg width="12" height="12" viewBox="0 0 12 12"><circle cx="6" cy="6" r="6" fill="#2e9b3a"/><path d="M3.3 6.2l1.8 1.8 3.6-3.8" stroke="#fff" stroke-width="1.4" fill="none"/></svg>Council &amp; high-standard grounds care</li>
      </ul>
      <span class="btn">Learn More About Us</span>
    </div>
  </div>
</section>

<section class="how">
  <div class="wrap">
    <h2 class="display section-title" style="color:#fff">How It <span class="accent">Works</span></h2>
    <div class="steps">
      <svg class="how-path" width="976" height="80" viewBox="0 0 976 80" fill="none" stroke="#c9d8c6" stroke-width="1.5" stroke-dasharray="4 5"><path d="M200 40 C260 0 380 0 440 30"/><path d="M540 30 C620 80 720 60 780 30"/></svg>
      <div class="step">
        <svg width="46" height="46" viewBox="0 0 46 46" fill="none" stroke="#fff" stroke-width="2"><rect x="10" y="8" width="26" height="32" rx="2"/><rect x="17" y="4" width="12" height="7" rx="1"/><path d="M15 20l3 3 5-6M15 31l3 3 5-6M27 21h5M27 32h5"/></svg>
        <h3>1. Inspect</h3><p>We evaluate your turf's condition to identify what it needs for peak performance</p>
      </div>
      <div class="step">
        <svg width="46" height="46" viewBox="0 0 46 46" fill="none" stroke="#fff" stroke-width="2"><rect x="8" y="12" width="30" height="26" rx="2"/><path d="M8 19h30M15 8v8M31 8v8M14 26h6M24 26h8M14 32h10"/></svg>
        <h3>2. Planning</h3><p>We create a tailored turf management plan to achieve healthy, high-performing fields</p>
      </div>
      <div class="step">
        <svg width="46" height="46" viewBox="0 0 46 46" fill="none" stroke="#fff" stroke-width="2"><circle cx="22" cy="9" r="4"/><path d="M22 13v12l-6 6M22 25l10 4M8 38h30M14 38l4-7h14l4 7"/></svg>
        <h3>3. Maintain</h3><p>We handle everything from mowing to fertilising, keeping your fields game-ready all year</p>
      </div>
    </div>
  </div>
</section>

<section class="products">
  <div class="wrap">
    <h2 class="display section-title">Our <span class="accent">Products</span></h2>
    <div class="card-row">
      <div class="prod"><div class="ph" role="img" aria-label="Hands holding rich dark soil" style="background:radial-gradient(circle at 50% 60%,#3a2a20,#7a5a48)"></div>
        <div class="prod-body"><h3>Premium Soil</h3><p>Build better turf with better soil. Our soil products restore balance, improve water movement, and keep your fields...</p>
        <div class="prod-foot"><span class="btn">Learn More</span><span class="price">$90/kg</span></div></div></div>
      <div class="prod"><div class="ph" role="img" aria-label="Green grass trimmer mowing a lawn" style="background:linear-gradient(180deg,#3f6a2c,#66a23d)"></div>
        <div class="prod-body"><h3>Grass Trimmer</h3><p>Designed for performance on every pass, the field trimmer makes it easy to achieve a smooth, uniform finish...</p>
        <div class="prod-foot"><span class="btn">Learn More</span><span class="price">$90/piece</span></div></div></div>
      <div class="prod"><div class="ph" role="img" aria-label="Gloved hand holding a turf sample" style="background:linear-gradient(180deg,#2f6e2a,#67a74a)"></div>
        <div class="prod-body"><h3>Turf Enhancers</h3><p>Enhance your field's performance naturally. These products strengthen turf health, promote balanced...</p>
        <div class="prod-foot"><span class="btn">Learn More</span><span class="price">$90/kg</span></div></div></div>
    </div>
    <div class="center" style="margin-top:36px"><span class="btn">See All Products</span></div>
  </div>
</section>

<section class="why">
  <div class="wrap">
    <div class="why-body">
      <h2 class="display">Why Choose <span class="accent">Us</span></h2>
      <p>At Brindle Grass Services, we deliver professional turf care with precision and pride. Our expert team uses proven methods, quality products, and tailored programs to keep every field performing at its best — from local sports grounds to high-standard council facilities.</p>
      <div class="features">
        <div class="feat"><svg width="22" height="22" viewBox="0 0 22 22" fill="none" stroke="#2e9b3a" stroke-width="1.6"><circle cx="11" cy="7" r="4"/><path d="M3 20c1-5 4-7 8-7s7 2 8 7"/></svg><div><h4>Professional Team</h4><p>Experienced experts you can trust for quality result</p></div></div>
        <div class="feat"><svg width="22" height="22" viewBox="0 0 22 22" fill="none" stroke="#2e9b3a" stroke-width="1.6"><circle cx="11" cy="9" r="6"/><path d="M8 14l-2 6 5-2 5 2-2-6"/></svg><div><h4>Premium Products</h4><p>Using top-quality turf care products for lasting results</p></div></div>
        <div class="feat"><svg width="22" height="22" viewBox="0 0 22 22" fill="none" stroke="#2e9b3a" stroke-width="1.6"><rect x="2" y="8" width="12" height="7" rx="1"/><path d="M14 10h4l2 3v2h-6"/><circle cx="6" cy="17" r="2"/><circle cx="17" cy="17" r="2"/></svg><div><h4>Modern Equipment</h4><p>Advanced tools for precise and efficient turf care</p></div></div>
        <div class="feat"><svg width="22" height="22" viewBox="0 0 22 22" fill="none" stroke="#2e9b3a" stroke-width="1.6"><path d="M4 18C4 9 10 4 19 4c0 9-5 15-14 15M4 18l8-8"/></svg><div><h4>Sustainable Practices</h4><p>Eco-friendly care for lasting turf health</p></div></div>
      </div>
    </div>
    <div class="ph" role="img" aria-label="Player in orange kit running on a field" style="background:linear-gradient(180deg,#b9c7c9 0%,#5c7a4e 35%,#2f5a31 100%)"></div>
  </div>
</section>

<section class="gallery">
  <div class="wrap">
    <h2 class="display section-title">Our <span class="accent">Gallery</span></h2>
    <div class="tabs"><span class="on">All</span><span>Cricket</span><span>Soccer</span><span>Rugby</span><span>Softball</span><span>Hockey</span><span>Tennis</span></div>
    <div class="grid">
      <div class="col">
        <div class="ph tall" role="img" aria-label="Player dribbling through agility hurdles" style="background:linear-gradient(180deg,#2c4f2e,#5e9a3c)"></div>
        <div class="ph short" role="img" aria-label="Players stretching on a field" style="background:linear-gradient(180deg,#4e6a3c,#7aa750)"></div>
      </div>
      <div class="col">
        <div class="ph short" role="img" aria-label="Players' feet with a ball on grass" style="background:linear-gradient(180deg,#7aa24f,#4f8a38)"></div>
        <div class="ph tall" role="img" aria-label="Players resting on turf with a city skyline" style="background:linear-gradient(180deg,#c6ccd0 0%,#8c9698 50%,#596b4b 100%)"></div>
      </div>
      <div class="col">
        <div class="ph tall" role="img" aria-label="Hockey player on a turf pitch" style="background:linear-gradient(180deg,#9aa3a8 0%,#a85a43 55%,#3e7a34 100%)"></div>
        <div class="ph short" role="img" aria-label="Coach and child with cones on a field" style="background:linear-gradient(180deg,#9bc2dd,#4c8e3a)"></div>
      </div>
    </div>
    <div class="center" style="margin-top:34px"><span class="btn">See All Photos</span></div>
  </div>
</section>

<section class="blog">
  <div class="wrap">
    <h2 class="display section-title">Latest <span class="accent">Blog</span></h2>
    <div class="card-row">
      <div class="post"><div class="ph" role="img" aria-label="Empty sports field with grandstand" style="background:linear-gradient(180deg,#5c8a4a,#3f7d2f)"></div>
        <div class="date"><svg width="12" height="12" viewBox="0 0 12 12" fill="none" stroke="#2e9b3a"><rect x="1" y="2" width="10" height="9" rx="1"/><path d="M1 5h10M4 1v2M8 1v2"/></svg>16 October, 2025</div>
        <h3>Fast Turf Recovery After Games</h3><p>Learn simple techniques to repair high-traffic areas and restore lush, even coverage...</p><span class="more">Learn More ⟶</span></div>
      <div class="post"><div class="ph" role="img" aria-label="Cricket ball resting on grass" style="background:linear-gradient(180deg,#8fc15a,#4e9a34)"></div>
        <div class="date"><svg width="12" height="12" viewBox="0 0 12 12" fill="none" stroke="#2e9b3a"><rect x="1" y="2" width="10" height="9" rx="1"/><path d="M1 5h10M4 1v2M8 1v2"/></svg>17 October, 2025</div>
        <h3>Smarter Watering Tips</h3><p>Save water and keep your turf greener with better moisture control...</p><span class="more">Learn More ⟶</span></div>
      <div class="post"><div class="ph" role="img" aria-label="Striped stadium pitch and running track" style="background:linear-gradient(180deg,#8fb0c4 0%,#4a8a36 50%,#b5533f 100%)"></div>
        <div class="date"><svg width="12" height="12" viewBox="0 0 12 12" fill="none" stroke="#2e9b3a"><rect x="1" y="2" width="10" height="9" rx="1"/><path d="M1 5h10M4 1v2M8 1v2"/></svg>18 October, 2025</div>
        <h3>Turf Health Secrets</h3><p>Simple steps to build stronger, longer-lasting playing surfaces</p><span class="more">Learn More ⟶</span></div>
    </div>
    <div class="center" style="margin-top:34px"><span class="btn">See All Blogs</span></div>
  </div>
</section>

<section class="faq">
  <div class="wrap">
    <div class="ph" role="img" aria-label="Player kicking a ball on a stadium pitch" style="background:linear-gradient(180deg,#9aa09a 0%,#3f6f34 45%,#2f6a2e 100%)"></div>
    <div class="faq-body">
      <h2 class="display">Common <span class="accent">Questions</span></h2>
      <div class="q"><div class="q-head">Can we purchase turf products directly from you?<span>+</span></div></div>
      <div class="q"><div class="q-head">How often should sports fields be maintained?<span>−</span></div><p>That depends on usage and field type — but regular inspections,<br>mowing, and nutrient programs are key to year-round performance.</p></div>
      <div class="q"><div class="q-head">Can you help with council or grant-funded projects?<span>+</span></div></div>
      <div class="q"><div class="q-head">Do you offer full turf management programs?<span>+</span></div></div>
      <div style="margin-top:26px"><span class="btn">Learn More About Us</span></div>
    </div>
  </div>
</section>

<section class="contact">
  <div class="wrap">
    <div class="form">
      <h2 class="display">Contact <span class="accent">Us</span></h2>
      <div class="field">Your Name</div>
      <div class="pair"><div class="field">Email</div><div class="field">Mobile No</div></div>
      <div class="field msg">Message...</div>
      <span class="btn">Send Now</span>
    </div>
    <div class="ph map" role="img" aria-label="Street map of the service area with a location pin" style="background:linear-gradient(120deg,#e7ede3 0%,#dfe8d9 60%,#9fcbe8 80%,#7ab8e2 100%)"></div>
  </div>
</section>

<footer class="site-footer">
  <div class="wrap">
    <div class="foot-cols">
      <div style="width:220px">
        <div class="brand" style="color:#fff;margin-bottom:16px"><i style="background:#fff"></i>Brindle Grass Services</div>
        <p>From soil testing to field renovation, Brindle Grass Services delivers complete turf care solutions for councils, clubs, and facilities across Harlow Bay.</p>
        <div class="socials"><i></i><i></i><i></i><i></i></div>
      </div>
      <div><h4>Quicklinks</h4><ul><li>Home</li><li>About Us</li><li>Services</li><li>Gallery</li><li>Products</li><li>Blog</li><li>Contact</li></ul></div>
      <div style="width:230px"><h4>Contact</h4>
        <p style="display:flex;gap:8px"><svg width="10" height="14" viewBox="0 0 10 14" fill="none" stroke="#fff" style="flex:none"><path d="M5 13S1 8 1 5a4 4 0 018 0c0 3-4 8-4 8z"/><circle cx="5" cy="5" r="1.5"/></svg>12 Fairway Road,<br>Harlow Bay 4799</p>
        <p style="display:flex;gap:8px;margin-top:14px"><svg width="13" height="10" viewBox="0 0 13 10" fill="none" stroke="#fff" style="flex:none"><rect x=".5" y=".5" width="12" height="9"/><path d="M.5 .5l6 5 6-5"/></svg>hello@brindlegrass.example</p>
      </div>
      <div style="width:216px"><h4>Newsletter</h4><p>Sign up and subscribe our newsletter</p>
        <div class="news"><span>Email</span><b>Subscribe</b></div></div>
    </div>
    <div class="copy">© 2025 Brindle Grass Services | Sports Turf Specialists | Harlow Bay</div>
  </div>
</footer>

</body>
</html>
```